Manufacturing business needs a website revamp

We are a manufacturing business supplying parts and modules to mid-high end consumer electronics brands from kitchen appliances to powered tools mainly in US/Europe. We want design ideas for a revamp of our website. We're aiming for a look and feel that's sleek, tidy and modern whilst still providing the right balance for content. A smooth and comfortable user experience that directs users to the information they may be looking for and promote our services. Something that incorporates design ideas such as: responsive design, lazy loading, slider banners, responsive layout, dynamic scrolling, liquid layout, full page headers etc... These are just terms bounced around within our team and certainly neither exclusive nor absolutely necessary. This is our current website for reference: https://www.varlumotek.com/ , which we feel is both outdated and doesn't engage visitors.

Attached is our planned new site map (we’re open to additional ideas here). We would like mock ups for each page on the site map. We will subsequently fill out the contents ourselves, but require design directions on e.g. how much text should go at which spot. E.g. for our Automotive page under Industries, we would like a suitable layout to be designed, as well as designated areas for texts. As for assets, please use any of the assets already on our current site or external source. We’ve yet to finalize on our selection of assets so please use the above as placeholders for now. Additionally, we would want a mock up for a pop-up frame to showcase additional technical specifications for some of our product ranges. For example, under the powertools section of our current website, we have additional listings under our product range. Currently they do not have a pop up function, but if we were to create a pop up frame to display detailed specifications, what layout should we use?

Finally, our target audiences are professional representatives from leading consumer brands who may be interested in our services. Our target customers are mid-high end brands. Think, for example, KVR/Harwick for automotive, Frostivane/Trell/Dovarin for consumer electronics/kitchen appliances, and Pelham Grove & Tasker/Brantover for powered tools. Typically it will be their product designers/engineers and supply chain representatives who will visit our website.

Target Market(s)

Professional product engineers/designers from mid-high end consumer electronics brands.

Industry/Entity Type

Manufacturing

Contact Information for Business Card

Attached are back and front of our current name card design. Again, we're open to changes that matches the style of our future website design. A few notes on the business card design:
- Cannot have blue background
- Does not have to be bilingual. I.e. open to single language design on one side and logo on the other

Coding

Coded - Design and coding required

Number of Pages Required

5+ page

Font styles to use
Sans Serif

Colors
3176b5

Requirements
Must have
• Color scheme must be based on the blue from our current website design. We will be keeping our current logo, hence must match that logo.
Nice to have
• Plim (or similar platforms) as demos/final solutions ok.
Should not have
• See brief

```html
<!DOCTYPE html>
<html lang="en">
<head>
<meta charset="utf-8">
<title>Varlumotek — Powering You Up For Success</title>
<link href="https://fonts.googleapis.com/css2?family=Poppins:wght@300;400;500;600&family=Bebas+Neue&display=swap" rel="stylesheet">
<style>
:root{
  --brand:#3176b5;
  --sky:#3d9be0;
  --deep:#0e5d98;
  --navy:#0b3d63;
  --ink:#1d2330;
  --muted:#6b7280;
  --line:#e3e8ee;
  --white:#ffffff;
}
*{box-sizing:border-box;margin:0;padding:0}
html,body{width:1200px;height:4082px;overflow:hidden}
body{position:relative;font-family:"Poppins",sans-serif;color:var(--ink);background:var(--white)}
.abs{position:absolute}
a{color:inherit;text-decoration:none}

/* header */
.site-header{position:absolute;left:0;top:0;width:1200px;height:75px;background:var(--white);z-index:5}
.brand{position:absolute;display:flex;align-items:center;gap:8px}
.brand-square{width:30px;height:30px;background:var(--sky);border-radius:4px}
.brand-name{font-weight:600;font-size:28px;color:var(--navy);line-height:1}
.brand-tag{position:absolute;font-size:7px;color:var(--navy);white-space:nowrap}
.main-nav{position:absolute;top:30px;left:385px;display:flex;gap:22px;font-size:12px;color:#333}
.main-nav .active{color:var(--sky)}
.call{position:absolute;left:880px;top:20px;display:flex;align-items:center;gap:12px}
.call-icon{width:34px;height:34px;border-radius:50%;background:var(--sky);display:flex;align-items:center;justify-content:center}
.call small{display:block;font-size:9px;color:#888}
.call strong{font-size:15px;font-weight:600;color:var(--navy)}

/* hero */
.hero{position:absolute;left:0;top:75px;width:1200px;height:638px;background:var(--deep);overflow:hidden}
.hero-photo{position:absolute;inset:0;border-bottom-left-radius:170px;
  background:linear-gradient(90deg,#e9eef2 0%,#dfe5ea 25%,#2b2f36 30%,#1b1e24 60%,#c9cfd6 63%,#2a2d33 70%,#1c1f25 90%,#eef1f3 100%)}
.hero-photo::after{content:"";position:absolute;left:0;right:0;bottom:0;height:170px;border-bottom-left-radius:170px;background:linear-gradient(180deg,rgba(240,243,246,0),#e4e9ee 60%)}
.hero-circle{position:absolute;left:584px;top:-50px;width:440px;height:440px;border-radius:50%;background:rgba(255,255,255,.94);border:6px solid rgba(61,155,224,.75);text-align:center;padding-top:150px}
.hero-title{font-family:"Bebas Neue",sans-serif;font-size:64px;line-height:.92;color:#1a1d22}
.hero-title span{color:var(--sky)}
.hero-text{font-size:13px;line-height:1.5;color:#333;margin:16px auto 0;width:360px}
.btn{display:inline-block;background:var(--sky);color:var(--white);font-size:14px;font-weight:500;border-radius:6px;text-transform:uppercase}
.hero .btn{margin-top:16px;padding:10px 20px}
.hotspot{position:absolute;width:20px;height:20px;border-radius:50%;background:var(--sky);border:2px solid var(--white);color:var(--white);font-size:14px;line-height:15px;text-align:center}
.dots{position:absolute;left:563px;top:592px;display:flex;gap:8px}
.dots i{width:11px;height:11px;border-radius:50%;background:#9ec9ee;border:2px solid var(--white)}
.dots i:first-child{background:var(--navy)}

/* welcome */
.welcome{position:absolute;left:0;top:713px;width:1200px;height:523px;background:var(--deep)}
.welcome h2{position:absolute;left:257px;top:70px;font-size:34px;font-weight:600;line-height:1.15;color:var(--white)}
.welcome .lead{position:absolute;left:258px;top:160px;font-size:13px;color:#d7e9f8}
.welcome .copy{position:absolute;left:586px;top:72px;width:370px;font-size:11px;line-height:1.75;color:#d7e9f8}
.welcome .copy p+p{margin-top:16px}
.welcome .btn{position:absolute;left:588px;top:244px;padding:10px 22px}
.showcase{position:absolute;left:288px;top:1073px;width:623px;height:338px;background:radial-gradient(circle at 55% 50%,#cfd6dc 0%,#eceef0 55%,#f1f2f3 100%)}

/* industries intro */
.section-title{font-size:32px;font-weight:500;color:var(--navy)}
.section-title span{color:var(--sky)}
.industries-intro .section-title{position:absolute;left:555px;top:1478px}
.industries-intro .sub{position:absolute;left:556px;top:1535px;width:350px;font-size:14px;line-height:1.6;color:var(--sky)}
.industries-intro .body{position:absolute;left:558px;top:1590px;width:360px;font-size:11px;line-height:2;color:#555}
.down-arrow{position:absolute;left:512px;top:1588px}

/* industry cards */
.ind-photo{position:absolute;top:1778px;height:300px}
.ind-card{position:absolute;top:2078px;height:263px;color:var(--white);text-align:center;padding:50px 40px 0}
.ind-card.light{background:var(--sky)}
.ind-card.dark{background:var(--deep)}
.ind-card h3{font-size:18px;font-weight:500}
.ind-card .tag{font-size:13px;line-height:1.5;margin-top:12px}
.ind-card .desc{font-size:10.5px;line-height:2;margin-top:12px;opacity:.95}
.ind-go{position:absolute;top:2320px;width:44px;height:44px;border-radius:50%;border:3px solid var(--white);display:flex;align-items:center;justify-content:center}

/* competencies */
.comp-head{position:absolute;left:0;top:2432px;width:1200px;text-align:center}
.comp-head p{font-size:13px;line-height:1.75;color:#444;margin-top:4px}
.tab{position:absolute;left:300px;width:217px;height:36px;border:1px solid var(--line);background:var(--white);font-size:11px;font-weight:500;color:#333;padding:11px 22px;box-shadow:0 1px 3px rgba(0,0,0,.05)}
.tab.active{background:var(--sky);color:var(--white);border-color:var(--sky)}
.tab.active::after{content:"";position:absolute;right:-9px;top:9px;border-left:9px solid var(--sky);border-top:9px solid transparent;border-bottom:9px solid transparent}
.comp-photo{position:absolute;left:563px;top:2580px;width:337px;height:121px;background:linear-gradient(120deg,#c9d6de 0%,#5d7382 40%,#1e2a33 75%,#3a4954 100%)}
.comp-cap{position:absolute;left:566px;top:2715px;width:340px}
.comp-cap h4{font-size:14px;font-weight:500;color:var(--sky)}
.comp-cap p{font-size:11px;line-height:1.75;color:#666;margin-top:8px}

/* question band */
.question{position:absolute;left:0;top:2921px;width:1200px;height:300px;background:linear-gradient(90deg,#0d5890,#0b4877 60%,#0c4f82)}
.question h2{position:absolute;left:253px;top:68px;font-size:32px;font-weight:500;color:var(--white)}
.question p{position:absolute;left:210px;top:124px;width:395px;font-size:12px;line-height:1.75;color:#dbeaf7;text-align:center}
.question .phone{position:absolute;left:268px;top:196px;display:flex;align-items:center;gap:12px;font-size:28px;font-weight:500;color:var(--white)}
.agent{position:absolute;left:690px;top:2853px;width:245px;height:368px;background:linear-gradient(180deg,#e9eef3,#c7d2dc);border-radius:120px 120px 0 0}

/* news */
.news-title{position:absolute;left:0;top:3288px;width:1200px;text-align:center}
.news-card{position:absolute;top:3366px;width:248px;text-align:center}
.news-photo{width:248px;height:165px}
.pill{display:inline-block;margin-top:27px;background:var(--sky);color:var(--white);font-size:13px;padding:6px 16px;border-radius:4px}
.news-card h4{font-size:12.5px;font-weight:600;line-height:1.55;margin-top:12px;color:#222}
.news-card .more{display:inline-block;margin-top:16px;font-size:11px;color:#888;text-decoration:underline}

/* footer */
.site-footer{position:absolute;left:0;top:3756px;width:1200px;height:281px;background:var(--navy);color:#d6e3ee}
.site-footer .brand-name{color:var(--white);font-size:34px}
.site-footer .brand-tag{color:#cfe0ee}
.foot-about{position:absolute;left:163px;top:122px;width:235px;font-size:11px;line-height:1.75}
.socials{position:absolute;left:163px;top:203px;display:flex;gap:6px}
.socials i{width:34px;height:32px;background:var(--sky);border-radius:3px}
.foot-col{position:absolute;top:66px}
.foot-col h5{font-size:14px;font-weight:500;color:var(--white);margin-bottom:20px}
.foot-col li{list-style:none;font-size:11px;line-height:22.5px;padding-left:16px;position:relative}
.foot-col li::before{content:"";position:absolute;left:0;top:9px;width:4px;height:4px;border-radius:50%;background:var(--sky)}
.contact-row{display:flex;gap:18px;font-size:11px;line-height:1.7;margin-bottom:14px}
.contact-row svg{flex:none;margin-top:2px}
.copyright{position:absolute;left:0;top:4037px;width:1200px;height:45px;background:var(--sky);color:var(--white);font-size:10px;text-align:center;line-height:45px}
</style>
</head>
<body>

<header class="site-header">
  <div class="brand" style="left:163px;top:14px">
    <span class="brand-square"></span><span class="brand-name">Varlumotek</span>
  </div>
  <span class="brand-tag" style="left:214px;top:55px">Powering You Up For Success</span>
  <nav class="main-nav">
    <a class="active" href="#">Home</a><a href="#">About Us</a><a href="#">Industries</a><a href="#">Core Competencies</a><a href="#">News</a><a href="#">Contact Us</a>
  </nav>
  <div class="call">
    <span class="call-icon"><svg width="16" height="16" viewBox="0 0 24 24"><path d="M6.6 10.8a15 15 0 0 0 6.6 6.6l2.2-2.2c.3-.3.7-.4 1-.2 1.1.4 2.3.6 3.6.6.6 0 1 .4 1 1V20c0 .6-.4 1-1 1A17 17 0 0 1 3 4c0-.6.4-1 1-1h3.5c.6 0 1 .4 1 1 0 1.3.2 2.5.6 3.6.1.3 0 .7-.2 1z" fill="#fff"/></svg></span>
    <div><small>Call Us On :</small><strong>(852) 3140 6628</strong></div>
  </div>
</header>

<section class="hero">
  <div class="hero-photo" role="img" aria-label="Bright modern kitchen with black cabinets, built-in ovens and appliances"></div>
  <div class="hero-circle">
    <h1 class="hero-title">Powering You<br>Up For <span>Success</span></h1>
    <p class="hero-text">Varlumotek is One of The Top Global Suppliers of Switches, Electronics Brands From Kitchen Appliances.</p>
    <a class="btn" href="#">Contact Us</a>
  </div>
  <div class="dots"><i></i><i></i><i></i><i></i></div>
</section>
<span class="hotspot" style="left:375px;top:307px">+</span>
<span class="hotspot" style="left:573px;top:343px">+</span>
<span class="hotspot" style="left:193px;top:389px">+</span>
<span class="hotspot" style="left:1117px;top:304px">+</span>
<span class="hotspot" style="left:1023px;top:426px">+</span>

<section class="welcome">
  <h2>Welcome To<br>Varlumotek</h2>
  <p class="lead">Powering you up for success.</p>
  <div class="copy">
    <p>Over four decades later, we continue to facilitate our customers' innovation and production across the world with a wide range of integration solutions, enabling our customers to keep ahead of the competition.</p>
    <p>To exceed customers' expectations with the most innovative technologies, the best cost effectiveness, and the utmost professional services.</p>
  </div>
  <a class="btn" href="#">Learn More</a>
</section>
<div class="showcase" role="img" aria-label="Computer monitor with machine gears emerging from the screen"></div>

<section class="industries-intro">
  <h2 class="section-title">Our <span>Industries</span></h2>
  <p class="sub">We Help Customers Improve Cost-Efficiency and Strengthen Innovation to Compete Globally</p>
  <p class="body">User interface and integrated module solutions with leading technology that serve automotive, electrical &amp; electronic and power tool industries among others</p>
  <svg class="down-arrow" width="14" height="118" viewBox="0 0 14 118"><path d="M7 0v115M1 108l6 7 6-7" stroke="#8bb8dc" stroke-width="1.2" fill="none"/></svg>
</section>

<div class="ind-photo" style="left:0;width:398px;background:linear-gradient(135deg,#3a4450,#1b2027 60%,#2c333c)" role="img" aria-label="Car climate control dials"></div>
<div class="ind-photo" style="left:398px;width:404px;background:linear-gradient(160deg,#6e6658,#2f2a24 55%,#4b3b2a)" role="img" aria-label="Living room with home appliances"></div>
<div class="ind-photo" style="left:802px;width:398px;background:linear-gradient(150deg,#5a4e40,#2d2823 50%,#9a7b56)" role="img" aria-label="Worker using a cordless drill on wood"></div>

<article class="ind-card light" style="left:0;width:398px">
  <h3>Automotive</h3>
  <p class="tag">One-Stop Solution From Design to Manufacturing</p>
  <p class="desc">Varlumotek expanded into automotive components market in 2006 through the acquisition of Norden Automotive GmbH, a German.</p>
</article>
<article class="ind-card dark" style="left:398px;width:404px">
  <h3>Home Appliance</h3>
  <p class="tag">Innovative solutions empower customers</p>
  <p class="desc">Varlumotek components have been widely adopted by the most trusted brands in home appliances, automotive, power tools...</p>
</article>
<article class="ind-card light" style="left:802px;width:398px">
  <h3>Power Tools</h3>
  <p class="tag">Highest Quality Standard And Innovative Solutions</p>
  <p class="desc">Varlumotek expanded into automotive components market in 2006 through the acquisition of Norden Automotive GmbH, a German</p>
</article>
<a class="ind-go" href="#" style="left:171px;background:var(--deep)"><svg width="18" height="12" viewBox="0 0 18 12"><path d="M0 6h16M11 1l5 5-5 5" stroke="#fff" stroke-width="1.6" fill="none"/></svg></a>
<a class="ind-go" href="#" style="left:578px;background:var(--sky)"><svg width="18" height="12" viewBox="0 0 18 12"><path d="M0 6h16M11 1l5 5-5 5" stroke="#fff" stroke-width="1.6" fill="none"/></svg></a>
<a class="ind-go" href="#" style="left:982px;background:var(--deep)"><svg width="18" height="12" viewBox="0 0 18 12"><path d="M0 6h16M11 1l5 5-5 5" stroke="#fff" stroke-width="1.6" fill="none"/></svg></a>

<section>
  <div class="comp-head">
    <h2 class="section-title">Core <span>Competencies</span></h2>
    <p>Our commitment to your success is our drive to continuous<br>innovation and improvement.</p>
  </div>
  <div class="tab" style="top:2585px">Awards And Honors</div>
  <div class="tab active" style="top:2637px">Research &amp; Development</div>
  <div class="tab" style="top:2690px">Manufacturing Capabilities</div>
  <div class="tab" style="top:2742px">Quality Management</div>
  <div class="comp-photo" role="img" aria-label="Close-up of a circuit board with a chip held by a hand"></div>
  <div class="comp-cap">
    <h4>Research &amp; Development</h4>
    <p>Our passion for technology advancement ensures the most innovative solutions for our customers</p>
  </div>
</section>

<section class="question">
  <h2>Have Any Question?</h2>
  <p>Engineering expertise, flexible approach and solid financial position Provide customers with total solution from initial design to manufacturing.</p>
  <div class="phone"><svg width="34" height="34" viewBox="0 0 24 24"><path d="M6.6 10.8a15 15 0 0 0 6.6 6.6l2.2-2.2c.3-.3.7-.4 1-.2 1.1.4 2.3.6 3.6.6.6 0 1 .4 1 1V20c0 .6-.4 1-1 1A17 17 0 0 1 3 4c0-.6.4-1 1-1h3.5c.6 0 1 .4 1 1 0 1.3.2 2.5.6 3.6.1.3 0 .7-.2 1z" fill="#3d9be0"/></svg>(852) 3140 6628</div>
</section>
<div class="agent" role="img" aria-label="Support representative with headset pointing toward the phone number"></div>

<section>
  <div class="news-title"><h2 class="section-title">Latest <span>News</span></h2></div>
  <article class="news-card" style="left:203px">
    <div class="news-photo" style="background:linear-gradient(160deg,#d8dde2,#8a96a2 60%,#4a5560)" role="img" aria-label="Visitors touring a company showroom"></div>
    <span class="pill">September 2020</span>
    <h4>Southgate Robotics<br>Association visits Varlumotek</h4>
    <a class="more" href="#">Read More</a>
  </article>
  <article class="news-card" style="left:476px">
    <div class="news-photo" style="background:linear-gradient(180deg,#c9d3da,#b7a58a 55%,#5f7048)" role="img" aria-label="Historic university building"></div>
    <span class="pill">July 2020</span>
    <h4>Varlumotek and academia join<br>forces to drive innovation</h4>
    <a class="more" href="#">Read More</a>
  </article>
  <article class="news-card" style="left:750px">
    <div class="news-photo" style="background:linear-gradient(160deg,#3d9be0,#1d5f9a 60%,#22364a)" role="img" aria-label="Panel speakers seated on a conference stage"></div>
    <span class="pill">January 2020</span>
    <h4>Varlumotek invited to speak at<br>Halvard ILP Global Innovation</h4>
    <a class="more" href="#">Read More</a>
  </article>
</section>

<footer class="site-footer">
  <div class="brand" style="left:163px;top:42px">
    <span class="brand-square" style="width:40px;height:40px"></span><span class="brand-name">Varlumotek</span>
  </div>
  <span class="brand-tag" style="left:227px;top:88px">Powering You Up For Success</span>
  <p class="foot-about">To exceed customers' expectations with the most innovative technologies, the best cost effectiveness, and the utmost professional services.</p>
  <div class="socials"><i aria-label="Social profile"></i><i aria-label="Social profile"></i><i aria-label="Social profile"></i></div>

  <div class="foot-col" style="left:431px">
    <h5>Sitemap</h5>
    <ul><li>Home</li><li>About Us</li><li>Industries</li><li>Core Competencies</li><li>News</li><li>Contact Us</li></ul>
  </div>
  <div class="foot-col" style="left:623px">
    <h5>Contact Us</h5>
    <div class="contact-row"><svg width="16" height="16" viewBox="0 0 24 24"><path d="M6.6 10.8a15 15 0 0 0 6.6 6.6l2.2-2.2c.3-.3.7-.4 1-.2 1.1.4 2.3.6 3.6.6.6 0 1 .4 1 1V20c0 .6-.4 1-1 1A17 17 0 0 1 3 4c0-.6.4-1 1-1h3.5c.6 0 1 .4 1 1 0 1.3.2 2.5.6 3.6.1.3 0 .7-.2 1z" fill="#3d9be0"/></svg><span>(852) 3140 6628</span></div>
    <div class="contact-row"><svg width="16" height="16" viewBox="0 0 24 24"><rect x="2" y="5" width="20" height="14" rx="2" fill="#3d9be0"/><path d="M3 6l9 7 9-7" stroke="#0b3d63" stroke-width="1.5" fill="none"/></svg><span>lena.ho@varlumotek<br>.com</span></div>
    <div class="contact-row"><svg width="16" height="18" viewBox="0 0 24 26"><path d="M12 1a8 8 0 0 0-8 8c0 6 8 15 8 15s8-9 8-15a8 8 0 0 0-8-8z" stroke="#3d9be0" stroke-width="2" fill="none"/><circle cx="12" cy="9" r="3" fill="#3d9be0"/></svg><span>5/F Harbourline Industrial<br>Centre, 18 Kestrel St.,<br>Eastbay H.K.</span></div>
  </div>
  <div class="foot-col" style="left:851px">
    <h5>Quick Links</h5>
    <ul><li>Languages</li><li>Privacy Policy</li><li>Tearms &amp; Conditions</li><li>Inquiry</li></ul>
  </div>
</footer>
<div class="copyright">©VARLUMOTEK - 2020 All rights reserved.</div>

</body>
</html>
```